LETTERHEAD & ENVELOPE: eye-catching stationary design for our custom office furniture business

Our company recently rebranded and we are in need of new stationary. Specifically, we need branded letterhead for standard paper size (8.5” x 11”), and matching envelopes, size: #9.

All designs should incorporate our brand colors, brand typeface, and logo. Please view attached brand guidelines document for brand colors, and brand description.

Letterhead: 8.5” x 11” Must include CedarlineKTV Logo, Talbot Greaves Certified Dealer Logo, mailing address, phone number, website, and email address.

Envelope: 9.5” x 4.125” Must include CedarlineKTV Logo, mailing address, and Talbot Greaves Certified Dealer Logo.

Attached files include:

```html
<!DOCTYPE html>
<html lang="en">
<head>
<meta charset="utf-8">
<title>CedarlineKTV Envelope #9</title>
<link rel="stylesheet" href="https://fonts.googleapis.com/css2?family=Raleway:wght@300&family=Roboto:wght@400&display=swap">
<style>
  :root {
    --backdrop: #e6e6e6;
    --paper: #f3f3f3;
    --paper-edge: #dcdcdc;
    --brand-green: #5b786b;
    --ink-grey: #555a58;
    --dealer-red: #d8432c;
    --on-green: #eef2ef;
  }
  * { margin: 0; padding: 0; box-sizing: border-box; }
  html, body { width: 1200px; height: 795px; overflow: hidden; }
  body {
    background: var(--backdrop);
    position: relative;
    font-family: "Roboto", Arial, sans-serif;
  }
  .envelope {
    position: absolute;
    width: 760px;
    height: 330px;
    background: var(--paper);
    border: 1px solid var(--paper-edge);
    border-radius: 3px;
    box-shadow: 0 6px 18px rgba(0,0,0,0.08);
    overflow: hidden;
  }
  .envelope--front { left: 70px; top: 420px; }
  .envelope--back { left: 370px; top: 45px; }

  .brand-lockup {
    position: absolute;
    display: flex;
    align-items: center;
    gap: 14px;
  }
  .brand-dot {
    width: 34px; height: 34px;
    border-radius: 50%;
    background: var(--brand-green);
    flex: none;
  }
  .brand-name {
    font-family: "Raleway", Arial, sans-serif;
    font-weight: 300;
    font-size: 34px;
    letter-spacing: 0.5px;
    color: var(--brand-green);
    line-height: 1;
  }
  .envelope--front .brand-lockup { left: 40px; top: 36px; }

  .return-address {
    position: absolute;
    left: 40px; top: 150px;
    font-size: 14px;
    line-height: 1.35;
    color: var(--ink-grey);
  }

  .dealer-mark {
    position: absolute;
    right: 40px; bottom: 40px;
    display: flex;
    align-items: center;
    gap: 8px;
  }
  .dealer-dot {
    width: 24px; height: 24px;
    border-radius: 50%;
    background: var(--dealer-red);
  }
  .dealer-name {
    font-size: 14px;
    color: var(--dealer-red);
  }

  .flap { position: absolute; left: 0; top: 0; width: 760px; height: 330px; }
  .envelope--back .brand-lockup { left: 330px; top: 62px; }
  .envelope--back .brand-dot { background: var(--on-green); }
  .envelope--back .brand-name { color: var(--on-green); }
</style>
</head>
<body>
  <section class="envelope envelope--front" aria-label="Envelope front">
    <div class="brand-lockup">
      <span class="brand-dot"></span>
      <span class="brand-name">CedarlineKTV</span>
    </div>
    <address class="return-address" style="font-style:normal">
      418 NE Fernhill Ave, Suite<br>140 Portland, OR 97209
    </address>
    <div class="dealer-mark">
      <span class="dealer-dot"></span>
      <span class="dealer-name">Talbot Greaves Certified Dealer</span>
    </div>
  </section>

  <section class="envelope envelope--back" aria-label="Envelope back">
    <svg class="flap" viewBox="0 0 760 330" aria-hidden="true">
      <path d="M0 0 H760 V185 Q758 200 740 198 C600 180 520 150 420 150 C300 150 200 110 80 60 C30 40 0 35 0 30 Z" fill="var(--brand-green)"/>
    </svg>
    <div class="brand-lockup">
      <span class="brand-dot"></span>
      <span class="brand-name">CedarlineKTV</span>
    </div>
  </section>
</body>
</html>
```